Business card for Northland's Blue Wagon.

Good day i am looking for a business card design for my business.
The name of the business is Northland's Blue Wagon. It is a van rental business that provides a driver and helper to the customer. Customer have use to van for small moves, studio or 1 bedroom, Moving furniture like couch or kitchen cabinets.
We are available evenings, weekends and holidays.
the means to contact us is by phone at 628-947-2071; By emails at Oakridge@northlandsbluewagon.net; or by social media, Facebook and Instagram.
You can see attached pictures of the van and or logo.

```html
<!DOCTYPE html>
<html lang="en">
<head>
<meta charset="utf-8">
<title>Northland's Blue Wagon – Business Card</title>
<link rel="stylesheet" href="https://fonts.googleapis.com/css2?family=Montserrat:wght@500;600;700&display=swap">
<style>
  :root {
    --stage: #353535;
    --paper: #ffffff;
    --brand-red: #d42027;
    --ink: #111111;
    --faint: #ebebed;
  }
  * { box-sizing: border-box; margin: 0; padding: 0; }
  html, body {
    width: 1200px; height: 1200px; overflow: hidden;
    background: var(--stage);
    font-family: "Montserrat", Arial, sans-serif;
  }
  .card {
    position: absolute; left: 217px; width: 766px; height: 460px;
    overflow: hidden;
    box-shadow: 0 6px 18px rgba(0,0,0,.45);
  }
  .card-front { top: 101px; background: var(--paper); }
  .card-back  { top: 631px; background: var(--brand-red); }

  .brand-watermark {
    position: absolute; left: 330px; top: 150px; width: 400px;
    text-align: center; color: var(--faint);
    font-weight: 700; font-size: 30px; line-height: 1.3;
  }
  .person-name {
    position: absolute; left: 55px; top: 58px;
    color: var(--brand-red); font-weight: 700; font-size: 34px;
  }
  .person-title {
    position: absolute; left: 55px; top: 103px;
    color: var(--ink); font-weight: 600; font-size: 22px;
  }
  .divider {
    position: absolute; left: 51px; top: 219px; width: 664px; height: 3px;
    background: var(--brand-red);
  }
  .contact-list { position: absolute; left: 51px; top: 241px; list-style: none; }
  .contact-item {
    display: flex; align-items: center; height: 25px; margin-bottom: 14px;
    color: var(--ink); font-weight: 500; font-size: 20px;
  }
  .contact-icon {
    width: 25px; height: 25px; border-radius: 50%; background: var(--ink);
    flex: none; margin-right: 10px; display: flex; align-items: center; justify-content: center;
  }
  .availability-band {
    position: absolute; left: 0; top: 371px; width: 100%; height: 26px;
    background: var(--brand-red); color: var(--paper);
    font-weight: 500; font-size: 19px; letter-spacing: 3.1px;
    line-height: 26px; padding-left: 54px; white-space: nowrap;
  }
  .back-brand {
    position: absolute; inset: 0;
    display: flex; align-items: center; justify-content: center; gap: 14px;
  }
  .back-brand-dot { width: 40px; height: 40px; border-radius: 50%; background: var(--paper); }
  .back-brand-name { color: var(--paper); font-weight: 700; font-size: 34px; }
</style>
</head>
<body>
  <section class="card card-front">
    <div class="brand-watermark">Northland's Blue Wagon</div>
    <h1 class="person-name">Your Name</h1>
    <p class="person-title">Your Title</p>
    <div class="divider"></div>
    <ul class="contact-list">
      <li class="contact-item">
        <span class="contact-icon">
          <svg width="14" height="14" viewBox="0 0 24 24"><path fill="#fff" d="M6.6 10.8a15.1 15.1 0 0 0 6.6 6.6l2.2-2.2c.3-.3.7-.4 1-.2 1.1.4 2.3.6 3.6.6.6 0 1 .4 1 1V20c0 .6-.4 1-1 1A17 17 0 0 1 3 4c0-.6.4-1 1-1h3.5c.6 0 1 .4 1 1 0 1.3.2 2.5.6 3.6.1.3 0 .7-.2 1z"/></svg>
        </span>628-947-2071
      </li>
      <li class="contact-item">
        <span class="contact-icon">
          <svg width="14" height="14" viewBox="0 0 24 24"><path fill="#fff" d="M4 11h12.2l-5.6-5.6L12 4l8 8-8 8-1.4-1.4 5.6-5.6H4z"/></svg>
        </span>Oakridge@northlandsbluewagon.net
      </li>
      <li class="contact-item">
        <span class="contact-icon"></span>@northlandsbluewagon.net
      </li>
    </ul>
    <div class="availability-band">We are available in evenings, weekends and holidays</div>
  </section>

  <section class="card card-back">
    <div class="back-brand">
      <span class="back-brand-dot"></span>
      <span class="back-brand-name">Northland's Blue Wagon</span>
    </div>
  </section>
</body>
</html>
```